" MAIOR PARTE DO ATENDIMENTO SERÁ ONLINE, PODENDO OPTAR POR VISITAR AS FAZENDAS OU NÃO. DEVIDO O ATENDIMENTO AOS CLIENTES SER DE FORMA DIGITAL, MARCAMOS REUNIÃO ATRAVÉS DE VÍDEO CONFERÊNCIA, ASSIM TIRANDO SUAS DÚVIDAS E EXPLICANDO OS SERVIÇOS FORNECIDOS... TODAS AS INFORMAÇÕES OBTIDAS EM CONVERSA COM O CLIENTE SÃO UNIFICADAS COM AS INFORMAÇÕES QUE OBTEMOS ATRAVÉS DE IMAGENS DE SATÉLITE, E ATRAVÉS DE UMA RELATÓRIO CONSEGUIMOS EXPLICAR COMO ESTÁ A SUA FAZENDA, QUAL É O MELHOR MÉTODO DE MANEJO PARA A SAFRA, SE HÁ OU NÃO ÁREAS DEGRADADAS, EXPLICAMOS PARA ELE, QUAIS AS QUANTIDADE E QUAIS OS LOCAIS DEVERÃO RECEBER APLICAÇÃO DE ADUBO. A AGRICULTURA DE PRECISÃO NÃO É UM APARELHO ELA É UMA TÉCNICA PARA OTIMIZARMOS OS CUSTOS. DEIXAMOS DE TRATAR UMA PROPRIEDADE DE FORMA GERAL, E TRATAMOS CADA TALHÃO OU CADA PASTO DE FORMA DIFERENTE, DE ACORDO COM SUA NECESSIDADE, ASSIM DIMINUINDO CUSTOS E MELHORANDO A PRODUÇÃO DA PROPRIEDADE, E CONSEQUENTEMENTE, MELHORANDO O RETORNO FINANCEIRO DO PRODUTOR RURAL. "

```html
<!DOCTYPE html>
<html lang="pt-BR">
<head>
<meta charset="UTF-8">
<title>Verdal – Papel de Parede</title>
<link href="https://fonts.googleapis.com/css2?family=Montserrat:ital,wght@0,300;0,400;1,400&display=swap" rel="stylesheet">
<style>
  :root {
    --page-bg: #c9c9c9;
    --green-deep: #0f3a33;
    --green-mid: #1d4c42;
    --green-light: #3a6656;
    --gold-dark: #8a6a2c;
    --gold: #c9a45a;
    --gold-light: #ecd49a;
    --white: #f3f3ee;
  }
  * { margin: 0; padding: 0; box-sizing: border-box; }
  html, body {
    width: 1200px;
    height: 1200px;
    overflow: hidden;
    background: var(--page-bg);
    font-family: "Montserrat", sans-serif;
  }
  .wallpaper {
    position: absolute;
    left: 40px;
    top: 282px;
    width: 1120px;
    height: 636px;
    overflow: hidden;
    background: var(--green-deep);
  }
  .wallpaper__photo {
    position: absolute;
    inset: 0 0 22px 0;
    background:
      radial-gradient(ellipse 40% 55% at 55% 40%, rgba(90,120,100,0.55), transparent 70%),
      radial-gradient(ellipse 30% 50% at 15% 50%, rgba(70,100,80,0.4), transparent 70%),
      linear-gradient(180deg, var(--green-mid) 0%, var(--green-deep) 100%);
  }
  .brand {
    position: absolute;
    left: 62px;
    top: 296px;
    display: flex;
    align-items: center;
    gap: 34px;
  }
  .brand__square {
    width: 64px;
    height: 64px;
    background: var(--gold);
  }
  .brand__name {
    font-weight: 300;
    font-size: 66px;
    line-height: 1;
    letter-spacing: 22px;
    color: var(--white);
  }
  .tagline {
    position: absolute;
    left: 170px;
    top: 372px;
    font-size: 14px;
    font-weight: 400;
    letter-spacing: 4.5px;
    color: var(--gold-light);
  }
  .website {
    position: absolute;
    left: 62px;
    top: 568px;
    font-size: 19px;
    font-style: italic;
    font-weight: 400;
    letter-spacing: 1.5px;
    color: var(--white);
  }
  .gold-band {
    position: absolute;
    left: 0;
    right: 0;
    bottom: 16px;
    height: 6px;
    background: linear-gradient(90deg, var(--gold-dark), var(--gold-light) 45%, var(--gold) 70%, var(--gold-dark));
  }
</style>
</head>
<body>
  <main class="wallpaper">
    <div class="wallpaper__photo" role="img" aria-label="Foto em tom verde escuro de uma profissional com notebook em meio a uma plantação"></div>
    <div class="brand">
      <span class="brand__square"></span>
      <span class="brand__name">VERDAL</span>
    </div>
    <p class="tagline">AGRICULTURA DE PRECISÃO</p>
    <p class="website">www.verdalagro.com.br</p>
    <div class="gold-band"></div>
  </main>
</body>
</html>
```